Anselm business card

Business card for commercial photography , photographer specialized in advertising, architecture and interior photography, adventure imagery and camera work. 40 years old, worked for the last 20 years. Business card needs to convey a sense of confidence in work achieved. Card needs to be eye catching as will be left behind in many people's offices. Should also mention discreetly NLVG accredited photographer at the verso of the card. Phone number and website link must be apparent easily.

Target Market(s)

Advertising agencies, commercial photography representation

Industry/Entity Type

Architecture

Contact Information for Business Card

Phone number : +61 470 918 264
anselm.varnet@mailbrook.net
www.anselmvarnet.net

Font styles to use
Sans Serif

Requirements
Must have
• Email adress
• Website
• Phone number
• Name
• Photographer
Nice to have
• NLVG accredited photographer
Should not have
• Rond corners

```html
<!DOCTYPE html>
<html lang="en">
<head>
<meta charset="utf-8">
<title>Anselm Varnet – Business Card</title>
<link rel="stylesheet" href="https://fonts.googleapis.com/css2?family=Arimo:wght@700&family=Open+Sans:wght@400&display=swap">
<style>
  :root {
    --stage: #e9e5df;
    --card-dark: #232323;
    --band: rgba(28, 28, 30, 0.86);
    --ink-light: #ffffff;
    --ink-soft: #e4e4e4;
    --sky-top: #7f93ad;
    --sky-mid: #a9a7a6;
    --sky-glow: #e6a653;
    --land: #2f6a2a;
    --land-deep: #1d3f1a;
  }
  * { box-sizing: border-box; margin: 0; padding: 0; }
  html, body {
    width: 1200px; height: 960px; overflow: hidden;
    background: var(--stage);
  }
  .stage {
    position: relative; width: 1200px; height: 960px;
    display: flex; justify-content: center; align-items: center; gap: 80px;
  }
  .card {
    position: relative; width: 340px; height: 560px;
    overflow: hidden;
    box-shadow: 0 10px 30px rgba(0,0,0,0.18);
  }
  /* Front */
  .card--front { background: var(--sky-top); }
  .landscape-photo {
    position: absolute; inset: 0;
    background: linear-gradient(180deg,
      var(--sky-top) 0%,
      var(--sky-mid) 35%,
      var(--sky-glow) 55%,
      var(--sky-mid) 68%,
      var(--land) 80%,
      var(--land-deep) 100%);
  }
  .accreditation-band {
    position: absolute; left: 0; right: 0; top: 62px; height: 118px;
    background: var(--band);
    display: flex; flex-direction: column; justify-content: center;
    padding: 0 26px;
  }
  .accreditation-band p {
    font-family: "Arimo", Arial, sans-serif; font-weight: 700;
    color: var(--ink-light); font-size: 30px; line-height: 1.12;
    letter-spacing: 0.2px;
  }
  /* Back */
  .card--back { background: var(--card-dark); }
  .identity {
    position: absolute; left: 28px; right: 20px; bottom: 34px;
    color: var(--ink-light);
  }
  .identity__name {
    font-family: "Arimo", Arial, sans-serif; font-weight: 700;
    font-size: 30px; line-height: 1.05;
  }
  .identity__role {
    font-family: "Open Sans", Arial, sans-serif;
    font-size: 17px; color: var(--ink-soft); margin-bottom: 18px;
  }
  .contact-list { list-style: none; }
  .contact-list li {
    display: flex; align-items: center; gap: 10px;
    font-family: "Open Sans", Arial, sans-serif;
    font-size: 16px; color: var(--ink-soft); line-height: 1.6;
  }
  .contact-list svg { width: 17px; height: 17px; flex: none; fill: var(--ink-light); }
</style>
</head>
<body>
<main class="stage">
  <section class="card card--front">
    <div class="landscape-photo" role="img" aria-label="Landscape photograph of a sunset sky over green treetops and distant temples"></div>
    <div class="accreditation-band">
      <p>NLVG accredited</p>
      <p>photographer</p>
    </div>
  </section>

  <section class="card card--back">
    <div class="identity">
      <h1 class="identity__name">Anselm Varnet</h1>
      <p class="identity__role">Photographer</p>
      <ul class="contact-list">
        <li>
          <svg viewBox="0 0 20 20" aria-hidden="true"><path d="M2 4h16v12H2z M3.5 5.5 10 10.5 16.5 5.5v-.2H3.5z" fill-rule="evenodd"/></svg>
          anselm.varnet@mailbrook.net
        </li>
        <li>
          <svg viewBox="0 0 20 20" aria-hidden="true"><path d="M10 1.5a8.5 8.5 0 1 0 0 17 8.5 8.5 0 0 0 0-17zm0 2a6.5 6.5 0 0 1 6.4 5.5h-3c-.1-2-.6-3.8-1.4-5.1A6.5 6.5 0 0 1 10 3.5zm-2 .4C7.2 5.2 6.7 7 6.6 9h-3A6.5 6.5 0 0 1 8 3.9zM3.6 11h3c.1 2 .6 3.8 1.4 5.1A6.5 6.5 0 0 1 3.6 11zm4.9-2c.1-2.3.8-4 1.5-4.9.7.9 1.4 2.6 1.5 4.9zm0 2h3c-.1 2.3-.8 4-1.5 4.9-.7-.9-1.4-2.6-1.5-4.9zm3.5 5.1c.8-1.3 1.3-3.1 1.4-5.1h3a6.5 6.5 0 0 1-4.4 5.1z"/></svg>
          www.anselmvarnet.net
        </li>
        <li>
          <svg viewBox="0 0 20 20" aria-hidden="true"><circle cx="10" cy="6" r="4"/><path d="M2 18c0-4.4 3.6-7 8-7s8 2.6 8 7z"/></svg>
          +61 470 918 264
        </li>
      </ul>
    </div>
  </section>
</main>
</body>
</html>
```